redesign my website coralhopvoyages.net and make it user friendly

I already have a website, coralhopvoyages.net, and want a redesign in WordPress with Elementor Pro, using the same text/content. The goal is to improve:

Design quality (colors, fonts, spacing, visual flow)
User experience (easy navigation, clear offers)
Conversion readiness (calls-to-action, trust signals, booking flow)
Technical side (SEO basics, fast speed, full mobile responsiveness)

The site should look modern, clean, fun, engaging, interactive and optimized for speed and usability.

I would like the 11 page to be consolidate dto 6 as follows: Home (main landing, highlights)

Sailboat Trips (all packages, itineraries, pricing)
Boats (fleet details, features, photos)
How It Works (booking process, FAQs, travel info, what to expect)
Blog
Contact Us (form, WhatsApp, phone, etc.)

Target Market(s)

sailboat trip customers for San Blas Islands in Panama

Industry/Entity Type

Travel, Boat Tour Agency

Coding

Coded - Design and coding required

Number of Pages Required

3 page

Font styles to use
Sans Serif
Other font styles liked:
• Oswalg and sans serif

Colors
0054AA
0677BA
7BADD7
CADEEF
E8F1F8
0094D4
00A9DD
6FCCEA
C7EBF8
E9F6FB
FFC000
F8CF3A
FAE287
FDF2CF
FEFAEE
F0912C
F2A743
F7CA91
FBE8D2
FDF5EE

Requirements
Must have
• Home (main landing, highlights) Sailboat Trips (all packages, itineraries, pricing) Boats (fleet details, features, photos) How It Works (booking process, FAQs, travel info, what to expect) Blog (updates, travel tips, inspiration) Contact Us (form, WhatsApp, phone, etc.)
Nice to have
• I want it to look professionla and be very user friendy to entice people to contact me to book boat trips
Should not have
• a store

```html
<!DOCTYPE html>
<html lang="en">
<head>
<meta charset="utf-8">
<title>Coral Hop Voyages – San Blas Sailing</title>
<link href="https://fonts.googleapis.com/css2?family=Oswald:wght@500;600&family=Lato:ital,wght@0,400;0,700;1,400&display=swap" rel="stylesheet">
<style>
:root{
  --blue:#1f56a6;
  --blue-deep:#1a4c98;
  --orange:#e8923a;
  --navy:#0c1527;
  --ink:#1d1d1d;
  --muted:#555;
  --line:#d5dbe3;
  --sky:#e6eef8;
  --white:#fff;
}
*{box-sizing:border-box;margin:0;padding:0}
html,body{width:1200px;height:3580px;overflow:hidden}
body{position:relative;font-family:'Lato',sans-serif;color:var(--ink);background:var(--white)}
.abs{position:absolute}
h2.section-title{font-family:'Oswald',sans-serif;font-weight:600;font-size:42px;color:var(--blue);letter-spacing:.2px;position:absolute}
h2.section-title span{color:var(--orange)}
.btn{display:inline-flex;align-items:center;justify-content:center;background:var(--orange);color:#fff;font-weight:700;border-radius:30px;font-family:'Lato',sans-serif}

/* top bar */
.topbar{left:0;top:0;width:1200px;height:33px;background:var(--blue)}
.topbar-accent{left:330px;top:0;width:50px;height:33px;background:var(--orange);clip-path:polygon(40% 0,100% 0,60% 100%,0 100%)}
.topbar-accent2{left:352px;top:0;width:40px;height:33px;background:var(--white);clip-path:polygon(60% 0,100% 0,40% 100%,0 100%)}
.contact-item{top:7px;color:#fff;font-size:15px;display:flex;align-items:center;gap:9px}
.contact-item svg{width:17px;height:17px}
.socials{display:flex;gap:12px}
.social-dot{width:19px;height:19px;border-radius:50%;background:#fff}
.navbar{left:0;top:33px;width:1200px;height:78px;background:#fff}
.logo-badge{left:86px;top:-60px;width:226px;height:226px;border-radius:50%;background:#fff;display:flex;align-items:flex-end;justify-content:center;padding-bottom:40px;z-index:3}
.logo-name{font-family:'Oswald',sans-serif;font-weight:600;font-size:21px;color:var(--blue)}
.menu{left:314px;top:62px;display:flex;gap:27px;font-size:15px;color:#222}
.menu .active{color:var(--orange);text-decoration:underline;text-underline-offset:4px}
.nav-cta{left:954px;top:50px;width:135px;height:46px;font-size:17px;font-weight:400}

/* hero */
.hero{left:0;top:111px;width:1200px;height:560px;background:radial-gradient(ellipse at 50% 20%,#cfe7d8 0,#6cc4c4 12%,#1b8fa8 35%,#115f86 70%,#0b4668 100%)}
.hero-title{left:0;top:258px;width:1200px;text-align:center;font-family:'Oswald',sans-serif;font-weight:600;color:#fff;font-size:58px;line-height:66px;text-shadow:0 2px 8px rgba(0,0,0,.25)}
.hero-title em{display:block;font-style:italic}
.hero-cta{left:523px;top:419px;width:154px;height:46px;font-size:17px}
.hero-wave{left:0;top:560px;width:1200px;height:120px}

/* tours */
.tour-card{top:834px;width:309px;height:373px;border:1px solid #cfd6de;border-radius:10px;background:#fff;overflow:hidden;box-shadow:0 3px 10px rgba(0,0,0,.06)}
.tour-card .media{width:100%;height:308px;border-radius:10px 10px 0 0}
.tour-card h3{text-align:center;font-size:21px;font-weight:700;font-family:'Lato',sans-serif;margin-top:17px}
.tour-card.featured{border:2px solid var(--orange)}
.tour-card.featured .media{background:var(--blue);color:#fff;font-size:15px;line-height:26px;padding:50px 26px 0}
.tour-card.featured .media i{display:block;margin-top:12px;font-size:14px}
.tour-card.featured h3{color:var(--blue);font-weight:400}

/* featured */
.featured-bg{left:0;top:1290px;width:1200px;height:663px;background:linear-gradient(120deg,#dfe9f6,#c9dcf1 40%,#e3edf8 70%,#d1e1f3)}
.arrow-btn{width:28px;height:28px;border:1.5px solid var(--blue);border-radius:50%;display:flex;align-items:center;justify-content:center}
.arrow-btn svg{width:15px;height:15px}
.boat-card{left:110px;top:1440px;width:979px;height:428px;background:#fff;border:2px solid var(--orange);border-radius:12px;overflow:hidden}
.boat-media{left:0;top:0;width:489px;height:428px;background:linear-gradient(170deg,#3a8a4e 0,#5fb7a8 25%,#2aa3c1 45%,#157aa8 70%,#0e5b8a 100%)}
.boat-name{left:530px;top:52px;font-family:'Oswald',sans-serif;font-weight:500;font-size:29px}
.boat-tag{left:531px;top:104px;font-size:17px}
.boat-quote{left:531px;top:140px;width:410px;font-size:15px;line-height:26px;color:#444}
.specs{left:531px;top:234px;width:420px;height:62px;border:2px solid var(--line);border-radius:6px;display:flex;align-items:center;justify-content:space-around;font-size:17px}
.specs span{display:flex;align-items:center;gap:14px}
.specs svg{width:26px;height:26px}
.boat-btn{left:531px;top:322px;width:136px;height:46px;font-size:17px;font-weight:400}

/* booking */
.book-media{left:110px;top:2104px;width:448px;height:419px;border:3px solid var(--blue);border-radius:12px;background:linear-gradient(160deg,#2f95c2,#1b7bb0 50%,#15689c)}
.field{left:641px;width:448px;height:48px;border:1.5px solid #777;border-radius:6px;display:flex;align-items:center;gap:12px;padding-left:22px;color:#666;font-size:15px}
.field svg{width:17px;height:17px}
.field.tall{height:104px;align-items:flex-start;padding-top:14px}
.radios{left:641px;top:2433px;display:flex;gap:27px;font-size:15px;color:#444}
.radios span{display:flex;align-items:center;gap:10px}
.radios i{width:18px;height:18px;border:1.5px solid #666;border-radius:50%}
.submit{left:641px;top:2476px;width:211px;height:44px;font-size:17px}

/* testimonials */
.testi-bg{left:0;top:2609px;width:1200px;height:600px;background:linear-gradient(180deg,#d3e2f4,#c2d6ee 40%,#d6e4f4 80%,#e4edf8)}
.testi-card{top:2763px;width:310px;height:295px;background:#fff;border-radius:10px;padding:52px 22px 0}
.quote-mark{top:-22px;left:20px;font-family:Georgia,serif;font-size:70px;line-height:1;color:#6e9fd6}
.stars{color:var(--orange);font-size:17px;letter-spacing:1px}
.testi-card p{font-size:14.5px;line-height:26.5px;color:#444;margin-top:8px;height:133px;overflow:hidden}
.person{display:flex;align-items:center;gap:20px;margin-top:10px}
.avatar{width:70px;height:70px;border-radius:50%;background:linear-gradient(#cfd4da,#9ea7b1)}
.person b{display:block;font-size:18px;font-weight:700;margin-bottom:6px}
.person small{font-size:15px;color:#444}

/* footer */
.footer-wave{left:0;top:3130px;width:1200px;height:112px}
.footer{left:0;top:3238px;width:1200px;height:342px;background:var(--navy);color:#fff}
.footer-brand{left:111px;top:3408px;font-family:'Oswald',sans-serif;font-weight:600;font-size:22px;color:#fff}
.footer-mark{left:150px;top:3300px;width:68px;height:68px;border-radius:50%;background:#1e4f8e}
.footer h4{font-family:'Lato',sans-serif;font-weight:700;font-size:21px;color:var(--orange);position:absolute;border-bottom:2px solid var(--orange);padding-bottom:4px}
.flist{list-style:none;font-size:15px;line-height:34.5px;position:absolute}
.flist li::before{content:"";display:inline-block;width:6px;height:6px;background:var(--orange);border-radius:50%;margin-right:16px;vertical-align:middle}
.fcontact{left:905px;top:3333px;font-size:15px;line-height:34.5px;position:absolute}
.fcontact div{display:flex;gap:9px;align-items:flex-start}
.fcontact i{flex:none;width:19px;height:19px;border-radius:50%;background:var(--orange);margin-top:8px;display:flex;align-items:center;justify-content:center}
.fcontact i svg{width:11px;height:11px}
.footer-rule{left:111px;top:3538px;width:978px;height:1px;background:#3a4456}
.copyright{left:0;top:3550px;width:1200px;text-align:center;font-size:15px;color:#fff}
</style>
</head>
<body>

<!-- header -->
<div class="abs topbar"></div>
<div class="abs topbar-accent"></div>
<div class="abs topbar-accent2"></div>
<div class="abs contact-item" style="left:430px">
  <svg viewBox="0 0 20 20"><circle cx="10" cy="10" r="10" fill="#fff"/><rect x="5" y="6.5" width="10" height="7" fill="none" stroke="#1f56a6" stroke-width="1.4"/><path d="M5 7l5 4 5-4" fill="none" stroke="#1f56a6" stroke-width="1.4"/></svg>
  hello@coralhopvoyages.net
</div>
<div class="abs contact-item" style="left:671px">
  <svg viewBox="0 0 20 20"><circle cx="10" cy="10" r="10" fill="#fff"/><path d="M7 5.5l2 2-1 1.5c.7 1.4 1.6 2.3 3 3l1.5-1 2 2-1.2 1.6C10 14.5 6 10.5 5.5 6.7z" fill="#1f56a6"/></svg>
  +573005550148
</div>
<div class="abs socials" style="left:1005px;top:7px"><i class="social-dot"></i><i class="social-dot"></i><i class="social-dot"></i></div>

<header class="abs navbar"></header>
<div class="abs logo-badge"><span class="logo-name">Coral Hop Voyages</span></div>
<nav class="abs menu">
  <span class="active">Home</span><span>Guna Yala</span><span>Fleet</span><span>About Us</span><span>Book Now</span><span>Pricing</span><span>Itineraries</span><span>Blog</span>
</nav>
<div class="abs btn nav-cta">Contact Us</div>

<!-- hero -->
<section class="abs hero" role="img" aria-label="Aerial view of a small palm island ringed by turquoise water with a catamaran sailing nearby"></section>
<h1 class="abs hero-title">San Blas Islands: Panama Sailing Vacations.<em>Ultimate Beaches &amp; Catamaran Tours</em></h1>
<div class="abs btn hero-cta">Inquire Now</div>
<svg class="abs hero-wave" viewBox="0 0 1200 120" preserveAspectRatio="none">
  <path d="M0 30 C300 -10 450 70 700 62 C900 55 1080 25 1200 0 V120 H0Z" fill="#fff"/>
  <path d="M0 30 C300 -10 450 70 700 62 C900 55 1080 25 1200 0 V12 C1080 40 900 75 700 80 C450 88 300 15 0 42Z" fill="#e8923a"/>
  <path d="M0 42 C300 20 450 95 700 92 C900 88 1080 55 1200 20 C1100 60 900 100 700 106 C450 110 300 45 0 55Z" fill="#1f56a6"/>
</svg>

<!-- tours -->
<h2 class="section-title" style="left:0;top:742px;width:1200px;text-align:center">Discover Ultimate <span>Panama Sailing Tours</span></h2>
<article class="abs tour-card" style="left:110px">
  <div class="media" role="img" aria-label="Sunset dinner table on a catamaran deck with tapas and a plant" style="background:linear-gradient(180deg,#d59a62,#8b7d7a 45%,#5a4a44)"></div>
  <h3>Private Charters</h3>
</article>
<article class="abs tour-card featured" style="left:445px">
  <div class="media">Share the experience with others for a more affordable alternative to a private charter. Perfect for couples, solo travelers, and small groups—enjoy San Blas beaches, clear waters, great meals, and a relaxed atmosphere with a welcoming crew.<i>Read More...</i></div>
  <h3>Shared Charters</h3>
</article>
<article class="abs tour-card" style="left:781px">
  <div class="media" role="img" aria-label="Group of smiling friends on a sailboat deck under the sail" style="background:linear-gradient(180deg,#d9d1c0,#8aa7c0 40%,#4d6f8f)"></div>
  <h3>Family Friendly Boat Trips</h3>
</article>

<!-- featured catamarans -->
<section class="abs featured-bg" role="img" aria-label="Faint underwater scene with tropical fish"></section>
<h2 class="section-title" style="left:108px;top:1355px">Featured <span>Catamarans</span></h2>
<div class="abs arrow-btn" style="left:1013px;top:1374px"><svg viewBox="0 0 16 16"><path d="M13 8H3m4-4L3 8l4 4" fill="none" stroke="#1f56a6" stroke-width="1.5"/></svg></div>
<div class="abs arrow-btn" style="left:1056px;top:1374px"><svg viewBox="0 0 16 16"><path d="M3 8h10M9 4l4 4-4 4" fill="none" stroke="#1f56a6" stroke-width="1.5"/></svg></div>
<article class="abs boat-card">
  <div class="abs boat-media" role="img" aria-label="Aerial view of a white catamaran anchored off a palm-lined beach"></div>
  <h3 class="abs boat-name">Marea 42</h3>
  <p class="abs boat-tag">Service that exceeds all expectations!</p>
  <p class="abs boat-quote">“We started as strangers and left as friends! The crew made sure everyone felt welcome, and every moment was filled with fun and laughter.”</p>
  <div class="abs specs">
    <span><svg viewBox="0 0 26 26"><path d="M3 3v20h20" fill="none" stroke="#1f56a6" stroke-width="3"/><path d="M7 23v-4M11 23v-6M15 23v-4M19 23v-6" stroke="#1f56a6" stroke-width="2"/></svg>42 ft</span>
    <span><svg viewBox="0 0 26 26"><path d="M3 15h20l-3 6H6z" fill="#1f56a6"/><rect x="8" y="8" width="10" height="6" fill="#1f56a6"/><rect x="11" y="4" width="4" height="4" fill="#1f56a6"/></svg>6 Cabin</span>
    <span><svg viewBox="0 0 26 26"><circle cx="9" cy="7" r="3.5" fill="#1f56a6"/><circle cx="18" cy="8" r="3" fill="#1f56a6"/><path d="M3 22c0-6 3-9 6-9s6 3 6 9zM14 22c0-5 2-8 4-8s5 3 5 8z" fill="#1f56a6"/></svg>10 Guest</span>
  </div>
  <div class="abs btn boat-btn">Info &amp; Price</div>
</article>

<!-- booking -->
<h2 class="section-title" style="left:0;top:2024px;width:1200px;text-align:center">Book an <span>Adventure</span></h2>
<div class="abs book-media" role="img" aria-label="Aerial view of a white catamaran with solar panels on deep blue water"></div>
<form>
  <div class="abs field" style="top:2104px"><svg viewBox="0 0 16 16"><circle cx="8" cy="5" r="3.5" fill="#777"/><path d="M1 16c0-5 3-7 7-7s7 2 7 7z" fill="#777"/></svg>Name</div>
  <div class="abs field" style="top:2173px"><svg viewBox="0 0 16 16"><rect x="1" y="3" width="14" height="10" fill="none" stroke="#777" stroke-width="1.5"/><path d="M1 3l7 6 7-6" fill="none" stroke="#777" stroke-width="1.5"/></svg>Email</div>
  <div class="abs field" style="top:2240px"><svg viewBox="0 0 16 16"><circle cx="8" cy="8" r="7.5" fill="#777"/><path d="M5.5 4.5l1.6 1.6-.8 1.2c.5 1.1 1.3 1.9 2.4 2.4l.8-.8 1.6 1.6-1 1.2C7.5 11.5 4.5 8.5 4.3 5.7z" fill="#fff"/></svg>Whatsapp Number</div>
  <div class="abs field tall" style="top:2305px"><svg viewBox="0 0 16 16"><ellipse cx="8" cy="7.5" rx="7.5" ry="6.5" fill="#777"/><path d="M3 12l-1 3 4-2z" fill="#777"/><circle cx="5" cy="7.5" r="1" fill="#fff"/><circle cx="8" cy="7.5" r="1" fill="#fff"/><circle cx="11" cy="7.5" r="1" fill="#fff"/></svg>Message</div>
  <div class="abs radios"><span><i></i>Private Charter</span><span><i></i>Shared Charter</span></div>
  <div class="abs btn submit">Submit</div>
</form>

<!-- testimonials -->
<section class="abs testi-bg" role="img" aria-label="Faded background of a catamaran moored near a palm island"></section>
<h2 class="section-title" style="left:111px;top:2683px">What They <span>Say</span></h2>
<div class="abs arrow-btn" style="left:1013px;top:2704px"><svg viewBox="0 0 16 16"><path d="M13 8H3m4-4L3 8l4 4" fill="none" stroke="#1f56a6" stroke-width="1.5"/></svg></div>
<div class="abs arrow-btn" style="left:1056px;top:2704px"><svg viewBox="0 0 16 16"><path d="M3 8h10M9 4l4 4-4 4" fill="none" stroke="#1f56a6" stroke-width="1.5"/></svg></div>

<article class="abs testi-card" style="left:111px">
  <span class="abs quote-mark">“</span>
  <div class="stars">★★★★★</div>
  <p>Everything was absolutely great — from the transfer to the boat crew, the food, and the islands we visited. We really enjoyed the whole experience. The only thing we regret is not having more time to stay.</p>
  <div class="person"><i class="avatar"></i><div><b>Clara &amp; Tom,</b><small>New York</small></div></div>
</article>
<article class="abs testi-card" style="left:445px">
  <span class="abs quote-mark">“</span>
  <div class="stars">★★★★★</div>
  <p>My family and I sailed with Captain Rafa and Luz on the Brisa Azul for 4 days. It was the best possible experience. Rafa took care of our EVERY needs as a family. Moreover, because we were traveling with kids.</p>
  <div class="person"><i class="avatar"></i><div><b>Marco &amp; Family,</b><small>New York</small></div></div>
</article>
<article class="abs testi-card" style="left:779px">
  <span class="abs quote-mark">“</span>
  <div class="stars">★★★★★</div>
  <p>My wife and I traveled from the UK to visit the San blas. Our 2 night 3 day trip on a catamaran was a once in a life time experience. It started with a smooth transfer from our hotel in Panama to the port.</p>
  <div class="person"><i class="avatar"></i><div><b>Helen</b><small>New York</small></div></div>
</article>

<!-- footer -->
<svg class="abs footer-wave" viewBox="0 0 1200 112" preserveAspectRatio="none">
  <path d="M0 80 C200 40 380 10 620 30 C820 48 1000 70 1200 40 V112 H0Z" fill="#0c1527"/>
  <path d="M0 62 C200 30 380 0 620 18 C820 36 1000 60 1200 28 V40 C1000 72 820 50 620 32 C380 12 200 45 0 80Z" fill="#1f56a6"/>
  <path d="M40 68 C220 40 400 22 620 40 C820 58 1000 84 1200 52 V64 C1000 95 820 72 620 56 C400 40 220 58 40 72Z" fill="#e8923a"/>
</svg>
<footer class="abs footer">
  <h4 style="left:364px;top:72px">Quick Links</h4>
  <ul class="flist" style="left:368px;top:95px"><li>Home</li><li>Guna Yala</li><li>Fleet</li><li>About Us</li><li>Book Now</li></ul>
  <ul class="flist" style="left:490px;top:95px"><li>Pricing</li><li>Itineraries</li><li>Activities</li><li>Blog</li><li>FAQs</li></ul>
  <h4 style="left:651px;top:72px">Help Links</h4>
  <ul class="flist" style="left:655px;top:95px"><li>Privacy Policy</li><li>Terms &amp; Conditions</li><li>Cookies</li></ul>
  <h4 style="left:905px;top:72px">Contact Us</h4>
</footer>
<i class="abs footer-mark"></i>
<div class="abs footer-brand">Coral Hop Voyages</div>
<div class="abs socials" style="left:126px;top:3482px;gap:17px"><i class="social-dot" style="width:23px;height:23px"></i><i class="social-dot" style="width:23px;height:23px"></i><i class="social-dot" style="width:23px;height:23px"></i></div>
<div class="fcontact">
  <div><i><svg viewBox="0 0 12 12"><path d="M3 1.5l1.6 1.6-.8 1.2c.5 1.1 1.3 1.9 2.4 2.4l.8-.8 1.6 1.6-1 1.2C4.5 8.5 2 6 1.8 2.7z" fill="#fff"/></svg></i>555.210.4476</div>
  <div><i><svg viewBox="0 0 12 12"><path d="M6 1a3.5 3.5 0 0 0-3.5 3.5C2.5 7 6 11 6 11s3.5-4 3.5-6.5A3.5 3.5 0 0 0 6 1z" fill="#fff"/></svg></i>1820 Harbor Lane, Portview,<br>TX 75000</div>
  <div><i><svg viewBox="0 0 12 12"><rect x="1.5" y="3" width="9" height="6" fill="none" stroke="#fff"/><path d="M1.5 3l4.5 3.5L10.5 3" fill="none" stroke="#fff"/></svg></i>info@coralhopvoyages.net</div>
</div>
<div class="abs footer-rule"></div>
<div class="abs copyright">Copyright 2025 © Coral Hop Voyages</div>

</body>
</html>
```